Startup online payment business - Sporting / Golf, Fairway Tally payment

Background:
Our business name is "Fairway Tally" we provide online payments for golfing services via our website. We currently have a logo used on our website. No other design style has been developed. Our aim is to remove cash payments for service at golf clubs.

Our Key Values:
Quick and easy
Formal and polite
Fun with professional boundary
Mate-ship relationships
100% online digital

What we want from you:
Marketing design to be used on posters and stickers in a retail setting to direct customers to our online payment Chanel.
Design must incorporate attached logo, URL fairwaytally.com.au and our key values can act as a guide the type of design. We have used color Hex#007672 for logo background. We are open to use other colors.

Target Market(s)

Golf clubs and golf players

Industry/Entity Type

Golf Course

Font styles to use
Sans Serif

Requirements
Must have
• Directions to online payment via URL: fairwaytally.com.au
Nice to have
• We like the idea of the slogan: No Cash - No worries. Have attached home screen that will be available from URL link. Consideration if using mobile phone in image. Push the online payment and steps 1. Visit fairwaytally.com 2. Select club 3. Confirm payment
Should not have
• Cartoons

```html
<!DOCTYPE html>
<html lang="en">
<head>
<meta charset="utf-8">
<title>Fairway Tally – Cashless Payments Poster</title>
<link rel="stylesheet" href="https://fonts.googleapis.com/css2?family=Bebas+Neue&family=Montserrat:wght@500;600&display=swap">
<style>
  :root {
    --canvas: #f2f1ee;
    --teal-deep: #0a5148;
    --teal: #0f6358;
    --teal-light: #1c7168;
    --white: #ffffff;
    --lime: #9cc63c;
    --soft-white: #e6efec;
  }
  * { margin: 0; padding: 0; box-sizing: border-box; }
  html, body {
    width: 1200px;
    height: 1000px;
    overflow: hidden;
    background: var(--canvas);
  }
  .poster {
    position: absolute;
    left: 290px;
    top: 40px;
    width: 621px;
    height: 920px;
    background: linear-gradient(160deg, var(--teal-light) 0%, var(--teal) 45%, var(--teal-deep) 100%);
    color: var(--white);
    text-align: center;
    box-shadow: 0 6px 18px rgba(0,0,0,0.18);
  }
  .poster > * {
    position: absolute;
    left: 0;
    width: 100%;
  }
  .brand {
    top: 52px;
    font-family: "Bebas Neue", sans-serif;
    font-size: 44px;
    letter-spacing: 2px;
    line-height: 1;
  }
  .headline {
    font-family: "Bebas Neue", sans-serif;
    font-size: 86px;
    line-height: 1;
    letter-spacing: 2px;
  }
  .headline--question { top: 188px; color: var(--white); }
  .headline--answer { top: 272px; color: var(--lime); }
  .tagline {
    top: 398px;
    font-family: "Montserrat", sans-serif;
    font-weight: 600;
    font-size: 17px;
    letter-spacing: 1.5px;
  }
  .tagline .accent { color: var(--lime); }
  .step__label {
    font-family: "Bebas Neue", sans-serif;
    font-size: 40px;
    letter-spacing: 1.5px;
    line-height: 1;
  }
  .step__text {
    font-family: "Montserrat", sans-serif;
    font-weight: 500;
    font-size: 22px;
    letter-spacing: 0.5px;
    line-height: 1;
    color: var(--soft-white);
  }
  .step--one .step__label { top: 467px; }
  .step--one .step__text { top: 516px; }
  .step--two .step__label { top: 582px; }
  .step--two .step__text { top: 630px; }
  .step--three .step__label { top: 703px; }
  .step--three .step__text { top: 752px; }
  .step { top: 0; height: 0; }
  .step > * { position: absolute; left: 0; width: 100%; }
  .site-url {
    top: 838px;
    font-family: "Montserrat", sans-serif;
    font-weight: 500;
    font-size: 28px;
    letter-spacing: 1.5px;
    color: var(--soft-white);
  }
</style>
</head>
<body>
  <main class="poster">
    <div class="brand">FAIRWAY TALLY</div>
    <h1 class="headline headline--question">NO CASH?</h1>
    <h2 class="headline headline--answer">NO WORRIES!</h2>
    <p class="tagline">CASHLESS PAYMENTS <span class="accent">IN 3 EASY STEPS</span></p>
    <section class="step step--one">
      <div class="step__label">STEP 1</div>
      <div class="step__text">Visit fairwaytally.com</div>
    </section>
    <section class="step step--two">
      <div class="step__label">STEP 2</div>
      <div class="step__text">Select Club</div>
    </section>
    <section class="step step--three">
      <div class="step__label">STEP 3</div>
      <div class="step__text">Confirm Payment</div>
    </section>
    <p class="site-url">FAIRWAYTALLY.COM.AU</p>
  </main>
</body>
</html>
```